looking for sleek business card to standout from the crowd!

We are a young biotechnology company looking to help you personalize your health through understanding your genetic make up. We need you help in making a clean but sleek business card design using our new logo. The goal? Any time we give our cards out, people say "nice card!" The feel we are going for is "modern-techy". We don't want to come across as an old, giant pharma company, but not trying to be a hipster either.

Target Market(s)

healthcare and biotechnology industry.

Industry/Entity Type

Biotechnology

Contact Information for Business Card

Info to include on the card will be NAME, TITLE, EMAIL, PHONE. The companies website (www.corvalinbio.com) should also be on the card some where. Would like the logo, when printed, to be raised.

Requirements
Must have
• The logo we have attached in the color it is in. Fonts for text should lean toward more professional/tech.
Nice to have
• Prefer white/light color background
Should not have
• cartoons, landscape backgrounds images.

```html
<!DOCTYPE html>
<html lang="en">
<head>
<meta charset="utf-8">
<title>Corvalin Business Card</title>
<link rel="stylesheet" href="https://fonts.googleapis.com/css2?family=Ubuntu:wght@400;500&display=swap">
<style>
  :root {
    --bg: #e9eaec;
    --card: #ffffff;
    --brand-blue: #1573bd;
    --brand-green: #8cc63f;
    --ink: #4a4a4a;
    --ink-soft: #5c5c5c;
  }
  * { margin: 0; padding: 0; box-sizing: border-box; }
  html, body { width: 1200px; height: 1200px; overflow: hidden; }
  body {
    background: var(--bg);
    font-family: "Ubuntu", sans-serif;
    position: relative;
  }
  .business-card {
    position: absolute;
    left: 100px; top: 314px;
    width: 1000px; height: 572px;
    background: var(--card);
    box-shadow: 0 6px 24px rgba(0,0,0,0.12);
  }
  .company-name {
    position: absolute; left: 70px; top: 72px;
    font-weight: 500; font-size: 52px; line-height: 1;
    color: var(--ink);
  }
  .person { position: absolute; left: 70px; top: 200px; }
  .person-name { font-size: 46px; font-weight: 500; line-height: 1; }
  .first-name { color: var(--brand-blue); }
  .last-name { color: var(--brand-green); }
  .person-title { font-size: 26px; color: var(--ink-soft); margin-top: 6px; }
  .divider {
    position: absolute; left: 70px; right: 70px; top: 300px;
    height: 2px; background: var(--brand-blue);
  }
  .contact-list {
    position: absolute; left: 70px; top: 330px;
    list-style: none;
  }
  .contact-item {
    display: flex; align-items: center; gap: 12px;
    font-size: 27px; color: var(--ink); height: 42px;
  }
  .contact-icon { width: 22px; height: 22px; fill: var(--brand-blue); flex: none; }
  .address {
    position: absolute; right: 70px; top: 452px;
    font-style: normal;
    text-align: right; font-size: 27px; color: var(--ink); line-height: 40px;
  }
  .address-line { display: flex; justify-content: flex-end; align-items: center; gap: 8px; }
  .address-line:last-child { padding-right: 30px; }
</style>
</head>
<body>
  <article class="business-card">
    <div class="company-name">CORVALIN</div>

    <div class="person">
      <div class="person-name"><span class="first-name">JOHN</span> <span class="last-name">DOE</span></div>
      <div class="person-title">Director</div>
    </div>

    <div class="divider"></div>

    <ul class="contact-list">
      <li class="contact-item">
        <svg class="contact-icon" viewBox="0 0 24 24"><path d="M6.6 10.8a15.1 15.1 0 0 0 6.6 6.6l2.2-2.2c.3-.3.7-.4 1-.2 1.1.4 2.3.6 3.6.6.6 0 1 .4 1 1V20c0 .6-.4 1-1 1C10.6 21 3 13.4 3 4c0-.6.4-1 1-1h3.5c.6 0 1 .4 1 1 0 1.3.2 2.5.6 3.6.1.3 0 .7-.2 1z"/></svg>
        <span>123-456-7890</span>
      </li>
      <li class="contact-item">
        <svg class="contact-icon" viewBox="0 0 24 24"><path d="M12 2a10 10 0 1 0 0 20 10 10 0 0 0 0-20zm6.9 6h-2.9a15.6 15.6 0 0 0-1.4-3.6A8 8 0 0 1 18.9 8zM12 4c.8 1.2 1.5 2.5 1.9 4h-3.8c.4-1.5 1.1-2.8 1.9-4zM4.3 14a8.2 8.2 0 0 1 0-4h3.4a16.5 16.5 0 0 0 0 4zm.8 2h2.9c.3 1.3.8 2.5 1.4 3.6A8 8 0 0 1 5.1 16zM8 8H5.1a8 8 0 0 1 4.3-3.6C8.8 5.5 8.3 6.7 8 8zm4 12c-.8-1.2-1.5-2.5-1.9-4h3.8c-.4 1.5-1.1 2.8-1.9 4zm2.3-6H9.7a14.7 14.7 0 0 1 0-4h4.6a14.7 14.7 0 0 1 0 4zm.3 5.6c.6-1.1 1.1-2.3 1.4-3.6h2.9a8 8 0 0 1-4.3 3.6zm1.7-5.6a16.5 16.5 0 0 0 0-4h3.4a8.2 8.2 0 0 1 0 4z"/></svg>
        <span>www.corvalinbio.com</span>
      </li>
      <li class="contact-item">
        <svg class="contact-icon" viewBox="0 0 24 24"><path d="M2 5h20v2l-10 6L2 7z"/><path d="M2 9l10 6 10-6v10H2z"/></svg>
        <span>John@corvalinbio.com</span>
      </li>
    </ul>

    <address class="address">
      <div class="address-line">
        <span>Dummy City</span>
        <svg class="contact-icon" viewBox="0 0 24 24"><path d="M12 3 2 12h3v8h5v-6h4v6h5v-8h3z"/></svg>
      </div>
      <div class="address-line">Dummy Country land</div>
    </address>
  </article>
</body>
</html>
```